Accounting Practice Business Card Design

I have a logo I am happy for you to use in the design of the Business Card.
You can edit and change colours as you please, I am not fixated on it.
I am looking for a modern and clean overall feel for the finished design.

The business is a small accounting practice who thrives on word of mouth referrals and this card will be given to all current and prospect clients.

Industry/Entity Type

Accountant

Contact Information for Business Card

Marcus Elwin
Level 5, 8 Corvale Ridge Road
ASHGROVE RISE VIC 3187
Phone: 9481 3057
Email: melwin@mrfaccountants.com.au
Web: www.mrfaccountants.com.au

Font styles to use
Serif
Sans Serif

Colors
0555a3
3277b5
85acd3
0393ce
33a6d7
85cae6
00a990
33b8a4
9bcb3c

Requirements
Must have
• "The end to your tax problems begin with us"
• "A referral from you is our greatest compliment"
Nice to have
• Modern clean professional

```html
<!DOCTYPE html>
<html lang="en">
<head>
<meta charset="utf-8">
<title>MRF Accountants – Business Card</title>
<link rel="stylesheet" href="https://fonts.googleapis.com/css2?family=Open+Sans:wght@400;600;700&display=swap">
<style>
  :root {
    --page: #ffffff;
    --frame-line: #8a8a8a;
    --card: #2c2c2c;
    --wordmark: #5a5a5a;
    --contact: #4f4f4f;
    --contact-shadow: #151515;
    --tagline: #e4e4e4;
    --web-light: #c9c9c9;
  }
  * { margin: 0; padding: 0; box-sizing: border-box; }
  html, body {
    width: 1200px; height: 1200px; overflow: hidden;
    background: var(--page);
    font-family: "Open Sans", Arial, sans-serif;
  }
  .sheet { position: relative; width: 1200px; height: 1200px; }
  .trim-frame {
    position: absolute; left: 177px; width: 846px; height: 531px;
    border: 1px solid var(--frame-line); background: var(--page);
  }
  .trim-frame--front { top: 34px; }
  .trim-frame--back { top: 635px; }
  .card {
    position: absolute; left: 18px; top: 18px; width: 810px; height: 495px;
    background: var(--card); border-radius: 10px; overflow: hidden;
  }
  .wordmark {
    position: absolute; left: 0; right: 0; text-align: center;
    color: var(--wordmark); font-weight: 700; line-height: 1;
  }
  .wordmark__name { display: block; }
  .wordmark__line { display: block; }
  .card--front .wordmark { top: 44px; }
  .card--front .wordmark__name { font-size: 112px; letter-spacing: 2px; }
  .card--front .wordmark__line { font-size: 34px; letter-spacing: 3px; margin-top: 10px; }
  .card--back .wordmark { top: 138px; }
  .card--back .wordmark__name { font-size: 140px; letter-spacing: 3px; }
  .card--back .wordmark__line { font-size: 43px; letter-spacing: 4px; margin-top: 12px; }
  .tagline {
    position: absolute; top: 237px; font-size: 14.5px;
    color: var(--tagline); white-space: nowrap;
  }
  .tagline--left { left: 43px; }
  .tagline--right { right: 43px; }
  .contact {
    position: absolute; left: 0; right: 0; top: 284px;
    text-align: center; list-style: none;
    color: var(--contact);
    text-shadow: 1px 2px 2px var(--contact-shadow);
  }
  .contact__name { font-size: 28px; font-weight: 600; line-height: 36px; }
  .contact__line { font-size: 22px; line-height: 31px; }
  .web-link {
    position: absolute; left: 0; right: 0; bottom: 34px;
    text-align: center; font-size: 16px; color: var(--web-light);
    letter-spacing: 0.3px;
  }
</style>
</head>
<body>
<main class="sheet">
  <section class="trim-frame trim-frame--front">
    <div class="card card--front">
      <div class="wordmark">
        <span class="wordmark__name">MRF</span>
        <span class="wordmark__line">ACCOUNTANTS</span>
      </div>
      <p class="tagline tagline--left">The end to your tax problems begin with us</p>
      <p class="tagline tagline--right">A referral from you is our greatest compliment</p>
      <ul class="contact">
        <li class="contact__name">Marcus Elwin</li>
        <li class="contact__line">Level 5, 8 Corvale Ridge Road</li>
        <li class="contact__line">ASHGROVE RISE VIC 3187</li>
        <li class="contact__line">9481 3057</li>
        <li class="contact__line">melwin@mrfaccountants.com.au</li>
        <li class="contact__line">www.mrfaccountants.com.au</li>
      </ul>
    </div>
  </section>
  <section class="trim-frame trim-frame--back">
    <div class="card card--back">
      <div class="wordmark">
        <span class="wordmark__name">MRF</span>
        <span class="wordmark__line">ACCOUNTANTS</span>
      </div>
      <p class="web-link">www.mrfaccountants.com.au</p>
    </div>
  </section>
</main>
</body>
</html>
```